Cedar Hollow responsive web design

We need a responsive, bootstrap compatible (but design only - PSD files) website design for a fly fishing shop and guide service.

Design should be very clean. Home Page design + interior page design please.

Possible Home Page Content:
Slide Show
Highlight Three Features: Guided Trips, Fly Shop, Missouri River
About

Thank you and good luck!

Shop

• This will be used on Bootstrap CMS so needs 12 column bootstrap measurements.

DESIGN ONLY NEEDED (clean PSD files), no programming required.
Need a Home Page layout and secondary page layout

Must show use of the following:
H1 - H5 font uses
link color
Dropdown for navigation bar
Button example
• No cutout images, this will be part of CMS and client needs to be able to update most content without knowing photoshop.

```html
<!DOCTYPE html>
<html lang="en">
<head>
<meta charset="utf-8">
<title>Cedar Hollow — Fly Fishing Shop &amp; Guide</title>
<link href="https://fonts.googleapis.com/css2?family=Open+Sans:wght@400;600;700&display=swap" rel="stylesheet">
<style>
  :root{
    --sky-top:#b4e4f7;
    --sky-bottom:#7ccdee;
    --ink:#111111;
    --nav-bg:#000000;
    --nav-active:#7fd0f2;
    --brand-blue:#1a83c6;
    --button-top:#3aa6e4;
    --button-bottom:#1c84c8;
    --body-text:#6b6b6b;
    --heading-dark:#1b1b1b;
    --rule:#e3e3e3;
    --footer-bg:#0f0f0f;
    --footer-accent:#8fd3f0;
    --white:#ffffff;
  }
  *{box-sizing:border-box;margin:0;padding:0}
  html,body{width:958px;height:1200px;overflow:hidden;background:var(--white)}
  body{position:relative;font-family:"Open Sans",Arial,sans-serif;color:var(--body-text)}
  .abs{position:absolute}

  /* Header */
  .site-header{left:0;top:0;width:958px;height:72px;background:linear-gradient(var(--sky-top),var(--sky-bottom))}
  .brand{left:110px;top:22px;font-weight:700;font-size:27px;color:var(--ink);letter-spacing:-.5px;line-height:1}
  .call-label{right:129px;top:22px;font-size:13px;color:var(--white);text-transform:uppercase}
  .call-number{right:129px;top:37px;font-size:19px;color:#1f5f86;letter-spacing:.5px}
  .main-nav{left:0;top:72px;width:958px;height:41px;background:var(--nav-bg)}
  .main-nav a{position:absolute;top:13px;font-weight:700;font-size:12.5px;color:var(--white);text-decoration:none;text-transform:uppercase}
  .main-nav a.active{color:var(--nav-active)}

  /* Hero */
  .hero{left:0;top:113px;width:958px;height:381px;background:linear-gradient(180deg,#b9b8c4 0%,#7d7569 22%,#5b5c3a 48%,#b58a66 62%,#6f6457 75%,#3f3c37 100%)}
  .hero-title{left:120px;top:233px;font-size:35px;color:var(--white);font-weight:400;letter-spacing:-.5px}
  .hero-sub{left:120px;top:279px;font-size:22px;color:var(--white);font-weight:400}
  .hero-copy{left:121px;top:314px;font-size:10px;line-height:16px;color:var(--white)}
  .btn{display:block;background:linear-gradient(var(--button-top),var(--button-bottom));color:var(--white);font-weight:600;font-size:9.5px;text-transform:uppercase;text-align:center;text-decoration:none;border-radius:2px}
  .hero-btn{left:120px;top:355px;width:85px;height:25px;line-height:25px}
  .dots{left:119px;top:395px}
  .dot{display:inline-block;width:8px;height:8px;border-radius:50%;background:rgba(255,255,255,.45);margin-right:3px}
  .dot.on{background:var(--white)}

  /* Features */
  .feature-frame{width:227px;height:99px;border:1px solid #e2e2e2;padding:4px;background:var(--white)}
  .feature-photo{width:100%;height:100%}
  .feature-title{font-size:18px;font-weight:600;color:var(--brand-blue)}
  .feature-copy{width:230px;font-size:9px;line-height:15.5px}
  .feature-btn{width:81px;height:23px;line-height:23px}

  .divider{left:120px;top:760px;width:723px;height:2px;background:var(--rule)}

  /* Lower columns */
  .col-title{font-size:21px;font-weight:400;color:var(--heading-dark)}
  .col-title.blue{color:var(--brand-blue)}
  .col-copy{font-size:9.6px;line-height:15.6px}
  .link-list{list-style:none}
  .link-list li{font-size:9.6px;font-weight:600;color:var(--brand-blue);line-height:19.2px}
  .link-list li::before{content:"\203A";font-weight:700;margin-right:6px}
  .news-title{font-size:13px;color:var(--brand-blue)}
  .dark-btn{left:121px;top:969px;width:89px;height:25px;line-height:25px;background:linear-gradient(#2b2b2b,#000);color:var(--white);font-weight:700;font-size:10px;text-align:center;border-radius:2px;text-transform:uppercase}

  /* Footer */
  .footer-accent{left:0;top:1066px;width:958px;height:6px;background:var(--footer-accent)}
  .site-footer{left:0;top:1072px;width:958px;height:128px;background:var(--footer-bg)}
  .footer-nav{left:121px;top:1106px;font-size:12px;font-weight:700;color:var(--white);text-transform:uppercase;word-spacing:1px}
  .footer-nav .sep{margin:0 9px;font-weight:400}
  .copyright{left:121px;top:1133px;font-size:10px;color:#9a9a9a}
  .social{width:23px;height:23px;border-radius:50%;background:var(--white);top:1105px}
</style>
</head>
<body>

<header class="abs site-header"></header>
<div class="abs brand">Cedar Hollow</div>
<div class="abs call-label">Call us now</div>
<div class="abs call-number">555.014.2231</div>

<nav class="abs main-nav">
  <a class="active" href="#" style="left:318px">Home</a>
  <a href="#" style="left:383px">About</a>
  <a href="#" style="left:453px">Guide Service</a>
  <a href="#" style="left:569px">Fly Shop</a>
  <a href="#" style="left:652px">Missouri River</a>
  <a href="#" style="left:773px">Contact</a>
</nav>

<section class="abs hero" role="img" aria-label="River photograph with pine-covered rocky hills and autumn shrubs reflected in calm water"></section>
<svg class="abs" style="left:56px;top:240px" width="36" height="74" viewBox="0 0 36 74" aria-hidden="true"><polyline points="33,2 3,37 33,72" fill="none" stroke="#fff" stroke-width="2"/></svg>
<svg class="abs" style="left:866px;top:240px" width="36" height="74" viewBox="0 0 36 74" aria-hidden="true"><polyline points="3,2 33,37 3,72" fill="none" stroke="#fff" stroke-width="2"/></svg>
<h1 class="abs hero-title">Fly fishing shop &amp; Guide</h1>
<h2 class="abs hero-sub">Lorem ipsum dolor sit consectetuer</h2>
<p class="abs hero-copy">Malesuada nec ultricies sit amet porttitor mattis enim in massa<br>libero interdum nec interdum vel blandit sed nulla</p>
<a class="abs btn hero-btn" href="#">Learn more</a>
<div class="abs dots"><span class="dot on"></span><span class="dot"></span><span class="dot"></span><span class="dot"></span></div>

<!-- Features -->
<div class="abs feature-frame" style="left:120px;top:511px"><div class="feature-photo" role="img" aria-label="Two anglers in a drift boat on the river" style="background:linear-gradient(135deg,#6d5a44,#2d2a26 60%,#8a8f86)"></div></div>
<h3 class="abs feature-title" style="left:120px;top:615px">Guided Trips</h3>
<p class="abs feature-copy" style="left:120px;top:638px">Aliquam nec erat at purus cursus interdum Vestibulum ligula augue bibendum accumsan vestibulum ut com­modo a mi Morbi ornare gravida</p>
<a class="abs btn feature-btn" href="#" style="left:120px;top:693px">Learn more</a>

<div class="abs feature-frame" style="left:369px;top:513px"><div class="feature-photo" role="img" aria-label="Interior of the fly shop with tackle displays" style="background:linear-gradient(135deg,#4a3d2c,#8a7152 50%,#2e3340)"></div></div>
<h3 class="abs feature-title" style="left:369px;top:616px">Fly Shop</h3>
<p class="abs feature-copy" style="left:369px;top:640px">Aliquam nec erat at purus cursus interdum Vestibulum ligula augue bibendum accumsan vestibulum ut com­modo a mi Morbi ornare gravida</p>
<a class="abs btn feature-btn" href="#" style="left:368px;top:693px">Learn more</a>

<div class="abs feature-frame" style="left:615px;top:513px"><div class="feature-photo" role="img" aria-label="Missouri River at sunset with mountains behind" style="background:linear-gradient(180deg,#6f6a70,#9a6a45 55%,#b85a25 70%,#3a3a42)"></div></div>
<h3 class="abs feature-title" style="left:615px;top:616px">Missouri River</h3>
<p class="abs feature-copy" style="left:615px;top:640px">Aliquam nec erat at purus cursus interdum Vestibulum ligula augue bibendum accumsan vestibulum ut com­modo a mi Morbi ornare gravida</p>
<a class="abs btn feature-btn" href="#" style="left:615px;top:693px">Learn more</a>

<div class="abs divider"></div>

<!-- What We Provide -->
<h3 class="abs col-title" style="left:121px;top:798px">What We Provide</h3>
<p class="abs col-copy" style="left:122px;top:831px;width:210px">Etiam eu urna Sed porta Suspendisse quam leo molestie sed luctus quis feugiat in pede Fusce tellus Sed metus augue convallis et vehicula ut pulvinar eu ante Integer orci tellus tristique vitae consequat nec porta vel lectus Nulla sit amet diam Duis non nunc</p>
<p class="abs col-copy" style="left:122px;top:928px;width:210px">libero a tempus libero lectus feugiat felis Morbi diam mauris viverra in gravida eu m</p>
<a class="abs dark-btn" href="#">View more</a>

<!-- Guide Services -->
<h3 class="abs col-title" style="left:369px;top:798px">Guide Services</h3>
<p class="abs col-copy" style="left:371px;top:830px;width:215px">Etiam eu urna Sed porta Suspendisse quam leo molestie sed luctus quis feugiat in pede</p>
<ul class="abs link-list" style="left:372px;top:871px">
  <li>Fusce tellus Sed metus augue</li>
  <li>Convallis et vehicula ut pulvinar eu ante</li>
  <li>Integer orci tellus tristique</li>
  <li>Vitae consequat nec porta vel lectus</li>
  <li>Nulla sit amet diam Duis non</li>
</ul>

<!-- Latest News -->
<h3 class="abs col-title blue" style="left:626px;top:797px">Latest News</h3>
<h4 class="abs news-title" style="left:626px;top:831px;font-weight:400">Etiam eu urna Sed porta</h4>
<p class="abs col-copy" style="left:626px;top:852px;width:220px">leo molestie sed luctus quis feugiat in pede Fusce tellus Sed metus augue convallis</p>
<h4 class="abs news-title" style="left:626px;top:899px;font-weight:400">Nunc tempus felis vitae</h4>
<p class="abs col-copy" style="left:626px;top:920px;width:220px">leo molestie sed luctus quis feugiat in pede Fusce tellus Sed metus augue convallis et vehicula ut pulvinar eu ante Integer</p>

<!-- Footer -->
<div class="abs footer-accent"></div>
<footer class="abs site-footer"></footer>
<div class="abs footer-nav">Home<span class="sep">|</span>About<span class="sep">|</span>Fly Shop<span class="sep">|</span>Guide Service<span class="sep">|</span>Missouri River<span class="sep">|</span>Contact</div>
<div class="abs copyright">© 2014 Company Name.&nbsp; All right reserved.&nbsp; Term of Use</div>
<span class="abs social" style="left:766px" aria-label="Social link"></span>
<span class="abs social" style="left:792px" aria-label="Social link"></span>
<span class="abs social" style="left:818px" aria-label="Social link"></span>

</body>
</html>
```